Nestiv app “nestiv application needs a business card design”

We need a business card design for new mobiles application
Nestiv app “for home furniture & decor design’’ all home furniture from many suppliers. We would like to see design should be reflects a app vision easy to choose the products
Should be:
Social media account’s and QR Code for application

```html
<!DOCTYPE html>
<html lang="en">
<head>
<meta charset="utf-8">
<title>Nestiv Business Card</title>
<link href="https://fonts.googleapis.com/css2?family=Work+Sans:wght@400;500;600&display=swap" rel="stylesheet">
<style>
  :root {
    --backdrop: #161616;
    --card: #262626;
    --card-edge: #2d2d2d;
    --accent: #7dc63a;
    --ink: #ffffff;
    --ink-soft: #e4e4e4;
  }
  * { box-sizing: border-box; margin: 0; padding: 0; }
  html, body {
    width: 1200px; height: 900px; overflow: hidden;
    background: var(--backdrop);
    font-family: "Work Sans", Arial, sans-serif;
  }
  .canvas {
    width: 1200px; height: 900px;
    display: flex; flex-direction: column;
    align-items: center; justify-content: center; gap: 40px;
  }
  .card {
    position: relative;
    width: 700px; height: 400px;
    background: linear-gradient(135deg, var(--card-edge), var(--card));
    border-bottom: 6px solid var(--accent);
    box-shadow: 0 12px 30px rgba(0,0,0,0.5);
  }
  .brand {
    display: flex; align-items: center; gap: 14px;
    color: var(--ink);
    font-weight: 500;
    letter-spacing: 1px;
  }
  .brand-mark {
    width: 22px; height: 22px;
    background: var(--accent);
  }
  .card-front {
    display: flex; flex-direction: column;
    align-items: center; justify-content: center; gap: 36px;
  }
  .card-front .brand { font-size: 84px; }
  .social-list { display: flex; gap: 14px; list-style: none; }
  .social-list li {
    width: 16px; height: 16px; border-radius: 50%;
    background: var(--accent);
  }
  .card-back { display: flex; align-items: center; }
  .card-back .brand {
    font-size: 64px;
    width: 340px; justify-content: center;
  }
  .divider {
    width: 2px; height: 190px;
    background: var(--accent);
    margin-right: 44px;
  }
  .contact { color: var(--ink-soft); font-size: 19px; line-height: 1.3; }
  .contact-name {
    color: var(--accent); font-weight: 500;
    font-size: 26px; letter-spacing: 1.5px; text-transform: uppercase;
  }
  .contact-role { font-size: 19px; margin-bottom: 18px; }
  .contact-address { font-style: normal; margin-bottom: 14px; }
  .contact-lines { list-style: none; }
  .contact-lines li { display: flex; align-items: center; gap: 10px; }
  .contact-lines svg { width: 14px; height: 14px; flex: none; }
</style>
</head>
<body>
<main class="canvas">
  <section class="card card-front">
    <div class="brand"><span class="brand-mark"></span>Nestiv</div>
    <ul class="social-list" aria-label="Social media accounts">
      <li></li><li></li><li></li><li></li><li></li>
    </ul>
  </section>

  <section class="card card-back">
    <div class="brand"><span class="brand-mark"></span>Nestiv</div>
    <div class="divider"></div>
    <div class="contact">
      <p class="contact-name">Daniel Reyes</p>
      <p class="contact-role">Director</p>
      <address class="contact-address">48 Alder Grove Lane<br>Maple Ridge, OR 97012</address>
      <ul class="contact-lines">
        <li>
          <svg viewBox="0 0 14 14" aria-hidden="true"><path d="M3 1 L5 1 L6 4 L4.5 5.2 Q5.8 8 8.8 9.5 L10 8 L13 9 L13 11 Q12 13 10 13 Q2 11 1 3 Q1 1 3 1 Z" fill="none" stroke="#7dc63a" stroke-width="1.2"/></svg>
          041 562 17 88
        </li>
        <li>
          <svg viewBox="0 0 14 14" aria-hidden="true"><rect x="1" y="3" width="12" height="8" fill="none" stroke="#7dc63a" stroke-width="1.2"/><path d="M1 3 L7 8 L13 3" fill="none" stroke="#7dc63a" stroke-width="1.2"/></svg>
          info@nestivapp.com
        </li>
        <li>
          <svg viewBox="0 0 14 14" aria-hidden="true"><circle cx="7" cy="7" r="6" fill="none" stroke="#7dc63a" stroke-width="1.2"/><ellipse cx="7" cy="7" rx="2.5" ry="6" fill="none" stroke="#7dc63a" stroke-width="1"/><path d="M1 7 H13" stroke="#7dc63a" stroke-width="1"/></svg>
          www.nestivapp.com
        </li>
      </ul>
    </div>
  </section>
</main>
</body>
</html>
```